RM Veltrano businesscard project

RM Veltrano Ltd is a freshly founded small (3 employees), young (average age is 30 years) company, living from the road transportation market without own tools.
We would like to have an impressive, new-line, cool busines card for a freshly founded forwarding company on an overcrowded market which raises attention and makes the potential partners eager to work with us.

Target Market(s)

The main profile of the company is logistic/forwarding on road.

Industry/Entity Type

Freight Forwarding

Contact Information for Business Card

Name: Berki Zsófia
Title: general manager
mobile nr: +36-70/482-5193
fax nr: +36-1/534-9061
e-mail: zsofia.berki@rmveltrano.example
info@rmveltrano.example
website address: http://www.rmveltrano.example
and if possible maybe some funny or helpful info on the back

Requirements
Must have
• contact details above
Nice to have
• some really nice and catching back-side (info, graphics, useful tool info... anything)
Should not have
• trucks, road, ship, airplane on it...

```html
<!DOCTYPE html>
<html lang="hu">
<head>
<meta charset="utf-8">
<title>RM Veltrano – Business Card</title>
<link rel="stylesheet" href="https://fonts.googleapis.com/css2?family=Encode+Sans+Condensed:wght@500&family=PT+Sans:wght@400&display=swap">
<style>
  :root {
    --brand-blue: #5584bf;
    --card-white: #ffffff;
    --back-grey: #bcbdbf;
    --ink-dark: #333333;
    --page-bg: #ebe9e5;
  }
  * { margin: 0; padding: 0; box-sizing: border-box; }
  html, body {
    width: 1200px;
    height: 1200px;
    overflow: hidden;
    background: var(--page-bg);
  }
  .canvas {
    position: relative;
    width: 1200px;
    height: 1200px;
  }
  .card {
    position: absolute;
    left: 212px;
    width: 773px;
    height: 437px;
    overflow: hidden;
  }
  .card--front { top: 125px; background: var(--card-white); }
  .card--back  { top: 638px; background: var(--back-grey); }

  /* Front bands */
  .band {
    position: absolute;
    left: 0;
    width: 506px;
    background: var(--brand-blue);
  }
  .band--title   { top: 0;     height: 106px; }
  .band--person  { top: 129px; height: 90px; }
  .band--contact { top: 244px; height: 193px; }

  .company-title {
    position: absolute;
    left: 56px;
    top: 22px;
    font-family: "Encode Sans Condensed", sans-serif;
    font-weight: 500;
    font-size: 56px;
    line-height: 1.2;
    letter-spacing: -0.5px;
    color: var(--card-white);
    white-space: nowrap;
  }
  .person-name {
    position: absolute;
    left: 60px;
    top: 148px;
    font-family: "PT Sans", sans-serif;
    font-size: 25px;
    line-height: 1.1;
    color: var(--card-white);
  }
  .person-role {
    position: absolute;
    left: 60px;
    top: 178px;
    font-family: "PT Sans", sans-serif;
    font-size: 18px;
    line-height: 1.1;
    color: var(--card-white);
  }
  .contact-list {
    position: absolute;
    left: 56px;
    top: 268px;
    list-style: none;
    font-family: "PT Sans", sans-serif;
    font-size: 18.5px;
    line-height: 25.6px;
    color: var(--card-white);
  }
  .contact-list li {
    display: flex;
    align-items: center;
    gap: 11px;
    white-space: nowrap;
  }
  .contact-icon {
    width: 17px;
    height: 17px;
    flex: none;
  }
  .brand-square {
    position: absolute;
    left: 581px;
    top: 158px;
    width: 120px;
    height: 120px;
    background: var(--brand-blue);
  }

  /* Back */
  .back-square {
    position: absolute;
    left: 327px;
    top: 88px;
    width: 120px;
    height: 120px;
    background: var(--brand-blue);
  }
  .back-name {
    position: absolute;
    left: 0;
    width: 100%;
    top: 262px;
    text-align: center;
    font-family: "Encode Sans Condensed", sans-serif;
    font-weight: 500;
    font-size: 58px;
    line-height: 1.2;
    letter-spacing: -0.5px;
    color: var(--ink-dark);
  }
  .back-web {
    position: absolute;
    left: 0;
    width: 100%;
    top: 392px;
    text-align: center;
    font-family: "PT Sans", sans-serif;
    font-size: 18.5px;
    line-height: 1.2;
    color: var(--ink-dark);
  }
</style>
</head>
<body>
<main class="canvas">

  <section class="card card--front" aria-label="Card front">
    <div class="band band--title"></div>
    <div class="band band--person"></div>
    <div class="band band--contact"></div>

    <h1 class="company-title">RM Veltrano</h1>
    <p class="person-name">Berki Zsófia</p>
    <p class="person-role">General Manager</p>

    <ul class="contact-list">
      <li>
        <svg class="contact-icon" viewBox="0 0 16 16" aria-hidden="true">
          <rect x="4" y="1" width="8" height="14" rx="1" fill="#fff"/>
          <rect x="5.5" y="3" width="5" height="5" fill="#5584bf"/>
        </svg>
        <span>+36-70/482-5193</span>
      </li>
      <li>
        <svg class="contact-icon" viewBox="0 0 16 16" aria-hidden="true">
          <rect x="4" y="1" width="8" height="5" fill="#fff"/>
          <rect x="1" y="6" width="14" height="8" rx="1" fill="#fff"/>
          <rect x="4" y="10" width="8" height="2" fill="#5584bf"/>
        </svg>
        <span>+36-1/534-9061</span>
      </li>
      <li>
        <svg class="contact-icon" viewBox="0 0 16 16" aria-hidden="true">
          <rect x="1" y="3" width="14" height="10" fill="#fff"/>
          <polyline points="1.5,3.5 8,9 14.5,3.5" fill="none" stroke="#5584bf" stroke-width="1.3"/>
        </svg>
        <span>zsofia.berki@rmveltrano.example</span>
      </li>
      <li>
        <svg class="contact-icon" viewBox="0 0 16 16" aria-hidden="true">
          <rect x="1" y="3" width="14" height="10" fill="#fff"/>
          <polyline points="1.5,3.5 8,9 14.5,3.5" fill="none" stroke="#5584bf" stroke-width="1.3"/>
        </svg>
        <span>info@rmveltrano.example</span>
      </li>
      <li>
        <svg class="contact-icon" viewBox="0 0 16 16" aria-hidden="true">
          <circle cx="8" cy="8" r="7" fill="#fff"/>
          <g fill="none" stroke="#5584bf" stroke-width="1">
            <ellipse cx="8" cy="8" rx="3" ry="7"/>
            <line x1="1" y1="8" x2="15" y2="8"/>
            <line x1="8" y1="1" x2="8" y2="15"/>
          </g>
        </svg>
        <span>http://www.rmveltrano.example</span>
      </li>
    </ul>

    <div class="brand-square" aria-hidden="true"></div>
  </section>

  <section class="card card--back" aria-label="Card back">
    <div class="back-square" aria-hidden="true"></div>
    <p class="back-name">RM Veltrano</p>
    <p class="back-web">www.rmveltrano.example</p>
  </section>

</main>
</body>
</html>
```